Private School social media templates / ads

We are a school in South Australia -around 40kms south of Adelaide. We have 2 campuses and need fresh looks for our social media advertising.

These ads need to be designed so that our team can use them and change headings as needed or images. Ideally, PSD files or InDesign files work best.

We would need you to use stock images initially so that we can then add student photos to the ads or, if you have a different suggestion we need to come up with fresh ideas to get our message across. Here is a bit of background:

A private Christian school - one campus in Morphett Vale in the south of Adelaide and our second campus in Aldinga - we are a smaller school compared to many larger ones, so our main focus of marketing is a messages along the lines of:
- Academic Excellence (see additional notes below on this topic)
- Respect and Values and Faith
- Student focused approach to teaching - smaller class sizes means no student is left behinid.

Parents give us feedback saying they like a school with good values and one that teaches respect but also is respectful. We have a strong no-bullying policy and our academics are excellent when comparing QELTAR data.

Note - Academic Excellence.
One thing I've tried to communicate is that academic excellence is not just about getting high marks, instead, it is about encouraging students to be the best they can be. So in the past headings like - Give your Child a Great Start - and similar have worked well. Also, a strong point is - At Northern Creek, your child is never just a number, but a valued part of our community.

These are some starting points. One thing I'd like to encourage is creativity - almost every school uses the same old style of advertising - a pic of 1 or 2 students and a heading like - Principals Tours - book now.

We need to stand out from the crowd when we advertise our tours.

The main focus is to increase enrolment numbers. We have a good quality CRM running so all enquiries go through a Pipeline Tracker.

I've included logos and brand documents - however, we are happy to move away from the fonts and be a bit creative with colours and tones we use.

Also, I have included a series we called -Seedling to Summit - where we created tech/space-themed ads showing where students could be in the future. This campaign ran for 2 years now and we need a fresh look with this sort of impact.

Target Market(s)

Primarily female aged 25-49

Industry/Entity Type

education - private school adelaide

Font styles to use
Sans Serif
Other font styles liked:
• Roboto is currently used but open to suggestions. Do not use Mutal Feelings font.

Requirements
Must have
• brand and promote school and school principal tours
Nice to have
• In our brand guide, there are our colours, ideally using those colors and tones for design
Should not have
• no generic ad designs - what I mean is a picture of a smiling student with the heading - Principal's Tours now on

```html
<!DOCTYPE html>
<html lang="en">
<head>
<meta charset="utf-8">
<title>Northern Creek Christian College – Social Ads</title>
<link rel="stylesheet" href="https://fonts.googleapis.com/css2?family=Anton&family=Oswald:wght@600;700&family=Poppins:ital,wght@0,400;0,500;0,600;0,700;1,600;1,700&display=swap">
<style>
  :root{
    --maroon:#7a1019;
    --maroon-dark:#5e0b12;
    --gold:#f7b50f;
    --yellow:#f6cf2f;
    --violet:#5a0a6b;
    --magenta:#b0108f;
    --royal:#1a5cc4;
    --floor:#e7eaee;
    --olive:#2d2910;
    --white:#ffffff;
    --ink:#1f1f1f;
    --skin:#e3b28f;
    --shirt:#49b8d0;
    --brand-blue:#1c8fd6;
  }
  *{box-sizing:border-box;margin:0;padding:0}
  html,body{width:1200px;height:1200px;overflow:hidden;background:#fff}
  body{position:relative;font-family:"Poppins",sans-serif}
  .ad{position:absolute;width:549px;height:549px;overflow:hidden;box-shadow:0 6px 18px rgba(0,0,0,.35)}
  .ad > *{position:absolute}
  .ad--excellence{left:38px;top:37px;background:radial-gradient(circle at 60% 40%,#8e1620,var(--maroon-dark))}
  .ad--values{left:612px;top:37px;background:radial-gradient(circle at 55% 45%,var(--magenta),var(--violet) 80%)}
  .ad--faith{left:38px;top:614px;background:linear-gradient(160deg,#14a0ea,var(--royal) 70%)}
  .ad--happy{left:612px;top:614px;background:radial-gradient(circle at 60% 60%,#fbe27a,var(--yellow) 60%)}

  .photo{border-radius:40% 40% 6px 6px;z-index:1}
  .photo--student-blonde{background:linear-gradient(180deg,#e8c98a 0%,var(--skin) 35%,var(--shirt) 70%,#3aa6c2 100%)}
  .photo--student-thinking{background:linear-gradient(180deg,#6a3b26 0%,#b07a58 25%,#234a3e 55%,#3e5f8a 100%)}

  .headline-art{left:0;top:0;width:549px;height:549px;z-index:3;overflow:visible}
  .headline-art text{font-family:"Anton",sans-serif}
  .headline-art .oswald{font-family:"Oswald",sans-serif;font-weight:700}

  .copy{z-index:3}
  .brand-name{font-family:"Poppins",sans-serif;font-weight:500;line-height:1.05;white-space:nowrap;z-index:3}
  .brand-mark{position:absolute;width:34px;height:34px;border-radius:50%;z-index:3}

  /* Ad 1 */
  .excellence__body{left:313px;top:292px;color:var(--white);font-size:24px;line-height:31px}
  .excellence__footer{left:0;top:468px;width:549px;height:81px;z-index:2}
  .excellence__brand{left:88px;top:494px;color:var(--ink);font-size:20px}
  .excellence__brand-mark{left:44px;top:497px;background:var(--maroon)}
  .cta{left:376px;top:497px;width:136px;height:38px;border-radius:19px;background:var(--maroon);color:var(--white);font-weight:700;font-size:13px;display:flex;align-items:center;justify-content:center;letter-spacing:.5px;z-index:3}

  /* Ad 2 */
  .values__brand{left:366px;top:75px;width:166px;text-align:center;color:var(--white);font-size:17px}
  .values__brand-mark{left:432px;top:33px;background:var(--white)}
  .values__body{left:110px;top:470px;width:330px;text-align:center;color:var(--white);font-size:19px;line-height:26px}

  /* Ad 3 */
  .faith__floor{left:0;top:413px;width:549px;height:136px;background:repeating-linear-gradient(90deg,var(--floor) 0 44px,#cfd4da 44px 46px)}
  .faith__bubble{left:366px;top:31px;width:150px;height:103px;border:2px solid var(--white);border-radius:50%;z-index:2}
  .faith__body{left:51px;top:292px;color:var(--white);font-size:24px;line-height:31px}
  .faith__brand{left:92px;top:484px;color:var(--brand-blue);font-size:17px}
  .faith__brand-mark{left:52px;top:485px;background:var(--brand-blue)}
  .chevrons{font-family:"Poppins",sans-serif;font-weight:700;letter-spacing:-3px;z-index:3}
  .faith__chevrons-top{left:244px;top:16px;color:var(--white);font-size:26px}
  .faith__chevrons-side{left:24px;top:388px;color:var(--gold);font-size:22px;line-height:14px;width:20px;text-align:center}

  /* Ad 4 */
  .happy__band{left:0;top:0;z-index:2}
  .happy__body{left:90px;top:130px;width:380px;text-align:center;color:var(--olive);font-weight:600;font-style:italic;font-size:14px;line-height:18px}
  .happy__brand{left:215px;top:490px;color:var(--white);font-size:21px}
  .happy__brand-mark{left:170px;top:497px;background:var(--white)}
  .happy__chevrons-top{left:18px;top:18px;color:var(--white);font-size:24px}
  .happy__chevrons-left{left:44px;top:372px;width:20px;text-align:center;color:var(--olive);font-size:22px;line-height:14px}
  .happy__chevrons-right{left:526px;top:316px;width:20px;text-align:center;color:var(--white);font-size:22px;line-height:14px}
</style>
</head>
<body>

<section class="ad ad--excellence">
  <div class="photo photo--student-blonde" style="left:11px;top:40px;width:290px;height:438px" role="img" aria-label="Smiling student with glasses holding a red folder"></div>
  <svg class="headline-art" viewBox="0 0 549 549" aria-label="Academic Excellence">
    <text x="236" y="143" font-size="92" fill="#f7b50f" textLength="283" lengthAdjust="spacingAndGlyphs" transform="rotate(-9.4 236 143)">Academic</text>
    <text x="244" y="208" font-size="86" fill="#ffffff" textLength="272" lengthAdjust="spacingAndGlyphs" transform="rotate(-9.4 244 208)">Excellence</text>
    <rect x="320" y="196" width="160" height="10" fill="#f7b50f" transform="rotate(-9.4 320 196)"/>
  </svg>
  <p class="copy excellence__body">Not just a score,<br>but a whole<br>educational<br>approach</p>
  <svg class="excellence__footer" viewBox="0 0 549 81" preserveAspectRatio="none">
    <path fill="#fff" d="M0 8 Q9 0 18 8 T36 8 T54 8 T72 8 T90 8 T108 8 T126 8 T144 8 T162 8 T180 8 T198 8 T216 8 T234 8 T252 8 T270 8 T288 8 T306 8 T324 8 T342 8 T360 8 T378 8 T396 8 T414 8 T432 8 T450 8 T468 8 T486 8 T504 8 T522 8 T540 8 T558 8 V81 H0Z"/>
  </svg>
  <span class="brand-mark excellence__brand-mark"></span>
  <p class="brand-name excellence__brand">Northern Creek<br>Christian College</p>
  <div class="cta">CONTACT US</div>
</section>

<section class="ad ad--values">
  <div class="photo photo--student-blonde" style="left:149px;top:31px;width:286px;height:354px;opacity:.9" role="img" aria-label="Smiling student with glasses holding a red folder"></div>
  <span class="brand-mark values__brand-mark"></span>
  <p class="brand-name values__brand">Northern Creek<br>Christian College</p>
  <svg class="headline-art" viewBox="0 0 549 549" aria-label="Values">
    <text x="120" y="467" font-size="160" fill="#f6cf2f" textLength="335" lengthAdjust="spacingAndGlyphs" transform="skewX(-10) translate(82 0)">VALUES</text>
  </svg>
  <p class="copy values__body">Helping your child navigate<br>and prepare for their future.</p>
</section>

<section class="ad ad--faith">
  <div class="faith__floor"></div>
  <span class="chevrons faith__chevrons-top">‹‹‹‹‹</span>
  <div class="faith__bubble" role="img" aria-label="Thought bubble picturing a stethoscope"></div>
  <div class="photo photo--student-thinking" style="left:250px;top:109px;width:299px;height:420px" role="img" aria-label="Thoughtful student sitting cross-legged with a laptop"></div>
  <svg class="headline-art" viewBox="0 0 549 549" aria-label="Faith and Focus">
    <text class="oswald" x="39" y="230" font-size="150" fill="#f6cf2f" textLength="201" lengthAdjust="spacingAndGlyphs">FAITH</text>
    <text class="oswald" x="36" y="282" font-size="64" fill="#ffffff" textLength="208" lengthAdjust="spacingAndGlyphs" transform="rotate(-8 36 282)">AND FOCUS</text>
  </svg>
  <p class="copy faith__body">Give your<br>child a great<br>start!</p>
  <span class="chevrons faith__chevrons-side">⌄<br>⌄<br>⌄<br>⌄</span>
  <span class="brand-mark faith__brand-mark"></span>
  <p class="brand-name faith__brand">Northern Creek<br>Christian College</p>
</section>

<section class="ad ad--happy">
  <span class="chevrons happy__chevrons-top">‹‹‹‹‹</span>
  <svg class="headline-art" viewBox="0 0 549 549" aria-label="Happy Students Enjoy Learning">
    <g transform="skewX(-10)">
      <text x="111" y="68" font-size="58" fill="#2d2910" textLength="355" lengthAdjust="spacingAndGlyphs">HAPPY STUDENTS</text>
      <text x="131" y="129" font-size="62" fill="#2d2910" textLength="341" lengthAdjust="spacingAndGlyphs">ENJOY LEARNING</text>
      <text x="128" y="126" font-size="62" fill="#ffffff" textLength="341" lengthAdjust="spacingAndGlyphs">ENJOY LEARNING</text>
    </g>
  </svg>
  <p class="copy happy__body">At Northern Creek you child is valued,<br>respected and cared for</p>
  <div class="photo photo--student-blonde" style="left:140px;top:168px;width:313px;height:330px" role="img" aria-label="Smiling student with glasses holding a red folder"></div>
  <svg class="happy__band" width="549" height="549" viewBox="0 0 549 549">
    <path fill="#2d2910" d="M0 460 Q280 490 549 410 V549 H0Z"/>
  </svg>
  <span class="chevrons happy__chevrons-left">⌄<br>⌄<br>⌄<br>⌄</span>
  <span class="chevrons happy__chevrons-right">⌃<br>⌃<br>⌃<br>⌃<br>⌃</span>
  <span class="brand-mark happy__brand-mark"></span>
  <p class="brand-name happy__brand">Northern Creek<br>Christian College</p>
</section>

</body>
</html>
```